RM Cargoline businesscard project

RM Cargoline Ltd is a freshly founded small (3 employees), young (average age is 30 years) company, living from the road transportation market without own tools.
We would like to have an impressive, new-line, cool busines card for a freshly founded forwarding company on an overcrowded market which raises attention and makes the potential partners eager to work with us.

Target Market(s)

The main profile of the company is logistic/forwarding on road.

Industry/Entity Type

Freight Forwarding

Contact Information for Business Card

Name: Berki Zsófia
Title: general manager
mobile nr: +36-70/482-5193
fax nr: +36-1/534-9061
e-mail: zsofia.berki@rmcargoline.example
info@rmcargoline.example
website address: http://www.rmcargoline.example
and if possible maybe some funny or helpful info on the back

Requirements
Must have
• contact details above
Nice to have
• some really nice and catching back-side (info, graphics, useful tool info... anything)
Should not have
• trucks, road, ship, airplane on it...

```html
<!DOCTYPE html>
<html lang="en">
<head>
<meta charset="utf-8">
<title>RM Cargoline – Business Card</title>
<link rel="stylesheet" href="https://fonts.googleapis.com/css2?family=Oswald:wght@400&family=Mulish:wght@400;800&display=swap">
<style>
  :root {
    --brand-blue: #4a76ad;
    --brand-blue-light: #5a84b8;
    --card-white: #ffffff;
    --ink: #111111;
    --backdrop: #e7e4df;
  }
  * { margin: 0; padding: 0; box-sizing: border-box; }
  html, body {
    width: 1200px;
    height: 1000px;
    overflow: hidden;
    background: var(--backdrop);
  }
  .card {
    position: absolute;
    left: 265px;
    width: 665px;
    height: 397px;
    box-shadow: 0 3px 10px rgba(0,0,0,.25);
  }
  .card--front { top: 73px; background: var(--brand-blue); color: var(--card-white); }
  .card--back { top: 533px; background: var(--card-white); color: var(--ink); }

  .wordmark {
    font-family: "Oswald", sans-serif;
    font-weight: 400;
    letter-spacing: -0.5px;
  }
  .card--front .wordmark {
    position: absolute;
    left: 31px;
    top: 22px;
    font-size: 58px;
    line-height: 1;
  }
  .brand-square {
    position: absolute;
    left: 390px;
    top: 55px;
    width: 215px;
    height: 288px;
    background: var(--brand-blue-light);
  }

  .person {
    position: absolute;
    left: 33px;
    top: 156px;
    font-family: "Mulish", sans-serif;
  }
  .person__name { font-weight: 800; font-size: 19px; letter-spacing: .3px; }
  .person__title { font-weight: 400; font-size: 16.5px; margin-top: 3px; }

  .contacts {
    position: absolute;
    left: 33px;
    top: 227px;
    list-style: none;
    font-family: "Mulish", sans-serif;
    font-size: 17px;
  }
  .contacts li {
    display: flex;
    align-items: center;
    height: 27px;
  }
  .contacts svg { width: 16px; height: 14px; margin-right: 9px; fill: var(--card-white); }

  .back-square {
    position: absolute;
    left: 270px;
    top: 65px;
    width: 116px;
    height: 154px;
    background: var(--brand-blue);
  }
  .card--back .wordmark {
    position: absolute;
    left: 0;
    right: 0;
    top: 245px;
    text-align: center;
    font-size: 60px;
    line-height: 1;
  }
  .tagline {
    position: absolute;
    left: 0;
    right: 0;
    top: 346px;
    text-align: center;
    font-family: "Mulish", sans-serif;
    font-size: 17px;
  }
</style>
</head>
<body>
  <section class="card card--front">
    <div class="wordmark">RM Cargoline</div>
    <div class="brand-square" aria-hidden="true"></div>

    <div class="person">
      <div class="person__name">BERKI ZSÓFIA</div>
      <div class="person__title">General Manager</div>
    </div>

    <ul class="contacts">
      <li>
        <svg viewBox="0 0 16 14" aria-hidden="true"><path d="M1 4c0-2 3-3 7-3s7 1 7 3v1h-3V3.5H4V5H1zM3 6h10l1 7H2z M6 8h4v3H6z"/></svg>
        +36-70/482-5193
      </li>
      <li>
        <svg viewBox="0 0 16 14" aria-hidden="true"><path d="M4 1h8v3H4zM1 5h14v6h-3v2H4v-2H1zM5 9v3h6V9z"/></svg>
        +36-1/534-9061
      </li>
      <li>
        <svg viewBox="0 0 16 14" aria-hidden="true"><path d="M1 2h14v10H1zM2.5 3.5 8 8l5.5-4.5v-.1H2.5z" fill-rule="evenodd"/></svg>
        info@rmcargoline.example
      </li>
      <li>
        <svg viewBox="0 0 16 14" aria-hidden="true"><path d="M1 2h14v10H1zM2.5 3.5 8 8l5.5-4.5v-.1H2.5z" fill-rule="evenodd"/></svg>
        zsofia.berki@rmcargoline.example
      </li>
      <li>
        <svg viewBox="0 0 16 14" aria-hidden="true"><path d="M1 1h14v10H9v1h2v1H5v-1h2v-1H1zm1.5 1.5v7h11v-7z" fill-rule="evenodd"/></svg>
        www.rmcargoline.example
      </li>
    </ul>
  </section>

  <section class="card card--back">
    <div class="back-square" aria-hidden="true"></div>
    <div class="wordmark">RM Cargoline</div>
    <p class="tagline">We Have Your Packages Covered</p>
  </section>
</body>
</html>
```